Bright Path Mentoring Brochure

Looking for a tri-fold brochure that can work as a self-mailer and a leave behind piece.

Bright Path Mentoring works with parents and young teens to develop personal capacity; emotional intelligence, resilience, communications skills, goal setting, and a high level of consciousness and attitude control. See our website at www.brightpathmentoring.example.

Cover should be provocative... quote about 46% of entering freshman from the website is powerful

We are talking about a 11"x8.5" opened, 3.7 x 8.5 folded tri-fold... there should be plenty of content on our website... The inside panels could be as follows

left panel could be a graphic and part of "the Story" Head line about 46% of entering freshman taking more than 6 years to get a degree.

Middle and right panels could be the three programs... Attitudinal Assessment, Group coaching on Communication, Value based S.M.A.R.T. goal setting and defeating internal blocks. and One on One Family coaching.

Target Market(s)

Parents and teens in the 9th grade age range

Industry/Entity Type

Communications

Requirements
Must have
• Provocative Title
"Did you know 46% of entering college freshman fail to receive a degree within 6 years?"
Powerful graphics to communicate transformation from anger and conflict between parents and teens to collaboration and cooperation.

```html
<!DOCTYPE html>
<html lang="en">
<head>
<meta charset="utf-8">
<title>Bright Path Mentoring – Tri-fold Brochure</title>
<link rel="stylesheet" href="https://fonts.googleapis.com/css2?family=Montserrat:wght@400;600;700&family=Didact+Gothic&display=swap">
<style>
:root{
  --bg:#e4e5e8;
  --navy:#234a78;
  --navy-dark:#1b3c66;
  --ink-blue:#1f3f8f;
  --green:#7e9a3a;
  --green-light:#93ad4c;
  --paper:#ffffff;
  --text:#4a4a4a;
  --muted:#6b6b6b;
  --photo-a:#5c5c5c;
  --photo-b:#c9c9c9;
}
*{box-sizing:border-box;margin:0;padding:0}
html,body{width:1200px;height:1193px;overflow:hidden}
body{background:var(--bg);font-family:"Didact Gothic",sans-serif;color:var(--text);position:relative}
.spread{position:absolute;left:230px;width:740px;height:572px;background:var(--paper);box-shadow:0 4px 14px rgba(0,0,0,.18);overflow:hidden}
.spread--outside{top:12px}
.spread--inside{top:602px}
.panel{position:absolute;top:0;height:100%;width:246.67px}
.panel--1{left:0}.panel--2{left:246.67px}.panel--3{left:493.33px}
.fold{position:absolute;top:0;bottom:0;width:1px;background:rgba(0,0,0,.08)}

/* outside */
.cover-quotes{background:var(--navy);color:#fff;text-align:center;padding:44px 26px 0}
.rule{width:90px;height:1.5px;background:#fff;margin:0 auto 14px}
.cover-quotes h3{font-family:"Montserrat",sans-serif;font-weight:600;font-size:11px;line-height:1.35;margin-bottom:18px}
.quote{font-size:8.5px;line-height:1.3;margin-bottom:13px;color:#dfe7f2}
.cover-quotes p.intro{font-size:9.5px;line-height:1.35;margin-top:26px}
.accent{color:var(--green-light)}
.photo{position:absolute;background:linear-gradient(120deg,var(--photo-b),var(--photo-a))}
.photo--cover{left:246.67px;top:0;width:493.33px;height:300px}
.band{position:absolute;background:var(--green)}
.band--cover{left:246.67px;top:300px;width:493.33px;height:30px}
.band--bottom{left:0;bottom:0;width:740px;height:8px}
.brand{display:flex;align-items:center;gap:8px;font-family:"Didact Gothic",sans-serif;font-size:18px;color:var(--text);position:absolute;white-space:nowrap}
.brand__dot{width:16px;height:16px;border-radius:50%;background:var(--green);flex:none}
.brand--light{color:#2b2b2b;left:20px;top:120px}
.contact-call{position:absolute;left:22px;top:180px;width:200px;font-size:10px;line-height:1.3;color:#fff}
.address{position:absolute;left:22px;top:352px;font-size:9px;line-height:1.35;color:var(--muted)}
.address strong{font-family:"Montserrat",sans-serif;color:var(--ink-blue);font-size:9px}
.contacts{position:absolute;left:22px;bottom:34px;font-size:8.5px;line-height:1.5;color:var(--muted)}
.contacts b{color:var(--ink-blue);display:inline-block;width:12px}
.did-you-know{position:absolute;left:18px;top:196px;width:215px;color:#fff}
.did-you-know h1{font-family:"Montserrat",sans-serif;font-weight:700;font-size:22px;margin-bottom:10px}
.did-you-know p{font-size:8.5px;line-height:1.35}
.attribution{position:absolute;left:18px;top:308px;font-size:8.5px;color:#fff}
.brand--cover{left:0;right:0;justify-content:center;top:378px}
.tagline{position:absolute;left:24px;top:420px;width:200px;text-align:center;font-size:9.5px;line-height:1.35;color:var(--muted)}

/* inside */
.story{position:absolute;left:0;top:0;width:740px;height:150px;background:var(--green)}
.story__rule{position:absolute;left:246.67px;top:150px;width:493.33px;height:3px;background:var(--ink-blue)}
.story-text{position:absolute;top:12px;width:222px;color:#fff;font-size:7.4px;line-height:1.35}
.story-text--1{left:14px}.story-text--2{left:258px;top:14px}.story-text--3{left:504px;top:14px}
.story-text h2{font-family:"Montserrat",sans-serif;font-weight:600;font-size:13px;margin-bottom:5px}
.leader{font-family:"Montserrat",sans-serif;font-size:12.5px;line-height:1.2;margin-top:10px}
.photo--story{left:0;top:116px;width:246.67px;height:110px;background:linear-gradient(120deg,#b58d6e,#e7e2dc 55%,#8a8f96)}
.program{position:absolute;width:224px;font-size:7.3px;line-height:1.33;color:var(--text)}
.program--1{left:12px;top:234px}
.program--2{left:258px;top:160px}
.program--3{left:504px;top:160px}
.program h4{font-family:"Montserrat",sans-serif;font-weight:600;font-size:8.2px;color:var(--ink-blue);margin-bottom:4px}
.program h5{font-family:"Montserrat",sans-serif;font-weight:600;font-size:7.6px;color:var(--ink-blue);margin:6px 0 3px}
.program h6{font-family:"Montserrat",sans-serif;font-weight:600;font-size:7.2px;color:#333;margin:5px 0 2px}
.program p{margin-bottom:5px}
.program em{font-style:italic}
.areas{display:grid;grid-template-columns:1fr 1fr;gap:0 8px;margin-bottom:5px;font-size:6.8px}
.band--inside{left:0;bottom:0;width:740px;height:6px;background:var(--ink-blue)}
</style>
</head>
<body>

<section class="spread spread--outside" aria-label="Brochure outside">
  <div class="panel panel--1 cover-quotes">
    <div class="rule"></div>
    <h3>Ask business executives to describe their recent entry-level hires and you may well hear statements like this…</h3>
    <p class="quote">“Academically superior, emotionally inferior”</p>
    <p class="quote">“Lack patience and persistence; easily thrown off their game”</p>
    <p class="quote">“Work to live, don’t live to work; disengage when things don’t go their way”</p>
    <p class="quote">“Entitled attitude; resent having to pay their dues”</p>
    <p class="quote">“Inflated sense of worth”</p>
    <p class="quote">“Do not understand the concept of no I in team”</p>
    <div class="rule" style="margin-top:22px"></div>
    <p class="intro">Self-awareness, emotional intelligence and the right attitude cannot start early enough. At <span class="accent">Bright Path Mentoring</span> we specialize in helping parents and their high school age kids to understand, appreciate and take effective action to build personal capacity as individuals. We instill the knowledge and skills that bring out the best in everyone and promote success in every aspect of life, for the rest of their lives.</p>
  </div>

  <div class="photo photo--cover" role="img" aria-label="Black and white photo of a frustrated teenage boy resting his head in his hand"></div>
  <div class="band band--cover"></div>

  <div class="panel panel--2">
    <div class="brand brand--light"><span class="brand__dot"></span>Bright Path Mentoring</div>
    <p class="contact-call">Please contact us today at Bright Path Mentoring to learn more about how our programs can help you and your teens get the most out of work, school and life!</p>
    <p class="address"><strong>Bright Path Mentoring</strong><br>218 Linden Avenue<br>Suite 4-B<br>Ashford, VA 20999</p>
    <p class="contacts"><b>p:</b> 555.014.2368<br><b>e:</b> kellyrt4success@example.com<br><b>w:</b> www.brightpathmentoring.example</p>
  </div>

  <div class="panel panel--3">
    <div class="did-you-know">
      <h1>Did you know?</h1>
      <p>“46% of college freshmen fail to get a degree within 6 years; for those who do, graduation is no guarantee of success.”</p>
    </div>
    <p class="attribution">- Harlow Education Foundation</p>
    <div class="brand brand--cover"><span class="brand__dot"></span>Bright Path Mentoring</div>
    <p class="tagline">It’s time to instill the knowledge and skills that promote success in every aspect of life, for the rest of their lives.</p>
  </div>

  <div class="fold" style="left:246.67px"></div>
  <div class="fold" style="left:493.33px"></div>
  <div class="band band--bottom"></div>
</section>

<section class="spread spread--inside" aria-label="Brochure inside">
  <div class="story"></div>
  <div class="story__rule"></div>
  <div class="photo photo--story" role="img" aria-label="Photo of a father and daughter working together at a computer"></div>

  <div class="story-text story-text--1">
    <h2>Our Story</h2>
    <p>In this age of right-sized staffs, tight budgets and squeezed profits employers are increasingly concerned about hiring recent grads whose personal capacity lags far behind their personal capability. It’s not the recent grads’ fault. They are behaving exactly as they were prepared to behave.</p>
  </div>
  <div class="story-text story-text--2">
    <p>The fact is, educational institutions, secondary and post-secondary, spend little if any time developing personal capacity in their students. They simply are not set up to do so. In the past, personal capacity was developed in the home and community. However, changing dynamics - single parent homes, two income homes and over-scheduled lives - have diminished the amount of emotional development being received by kids, especially</p>
  </div>
  <div class="story-text story-text--3">
    <p>those in the all-important 14-17 age range. This may explain why college dropout rates were called a “national crisis” in a January 2013 research report funded by the Harlow Education Foundation. But we’re ready to show you that…</p>
    <p class="leader">Everyone is a leader,<br>either by choice or default.</p>
  </div>

  <div class="program program--1">
    <h4>Program 1: Bright Path Assessment</h4>
    <p>The Bright Path Mentoring process begins with a comprehensive attitudinal assessment, of each team member individually and the team as a whole, using the highly respected Core Strength Index (CSI) assessment tool.</p>
    <p>The assessment tool is administered online and requires approximately 20 minutes to complete. It includes a comprehensive debrief for each individual and for the team conducted by a master practitioner trained and certified to administer and debrief the assessment.</p>
    <h5>What does the assessment tell us?</h5>
    <p>The Core Strength Index assessment provides insights into how you show up in various aspects of your life. It measures your potential leadership ability by your level of consciousness.</p>
    <p>The assessment measures your ability to lead people, including yourself, to take positive, productive and sustainable action. The assessment also measures how involved or engaged you are in your roles and tasks on the job, at school and at home.</p>
    <p>Finally, the assessment shows your energetic reaction to stress so that you can recognize and, if desired, modify that reaction.</p>
  </div>

  <div class="program program--2">
    <h4>Program 2: Bright Path Personal Coaching<br><em>13-Week, 26-Week and Full Year</em></h4>
    <h6><em>Pre-requisite - CSI Assessment and Debrief completed for individuals and team</em></h6>
    <p>Research indicates that successful, happy people have a high level of confidence and satisfaction in 14 specific areas including:</p>
    <div class="areas">
      <span>- Communication Skills<br>- Energy Level<br>- Engagement at School &amp; Work<br>- Family Relationships<br>- Financial Success<br>- Health &amp; Wellness<br>- Intimate Relationships</span>
      <span>- Leadership Ability<br>- Personal Freedom<br>- Productivity<br>- Spirituality<br>- Time Management<br>- Work/School/Life Balance<br>- Working Relationships</span>
    </div>
    <p>The Bright Path Mentoring Program is designed to build awareness, appreciation and confidence in each of these 14 areas with emphasis on those areas most relevant to the teen’s need at present.</p>
    <h5>Program Specifics</h5>
    <p><em>45-min. weekly one-on-one telephone call with teen<br>45-min. bi-weekly call with one or both parents<br>1-hour monthly in-person meeting with the team</em></p>
    <p>The agenda for each call is determined by the client. The coach will provide a “thought starter” via e-mail prior to each call to encourage the client to think about the call’s outcome. Some calls will result in a short assignment. All assignments are optional and may involve thinking about a specific question, a brief reading, writing or completing a coach supplied form.</p>
    <p>Individual participants have unlimited access to the coach via e-mail should questions or situations arise that the client wants to share with the coach.</p>
  </div>

  <div class="program program--3">
    <h4>Program 3: Bright Path Group Coaching Teens and Adults</h4>
    <h6><em>(3) 2.5 hour sessions held once a week for 3 weeks</em></h6>
    <h5>Session 1 - Effective Communication Workshop</h5>
    <p>In our Effective Communications Workshop you will grasp how to facilitate bridge-building, even when you have very different views of a situation, allowing you to resolve differences without anyone feeling like they’ve been bullied into a solution or demeaned or humiliated.</p>
    <p>Just as important, you’ll learn the basics of perhaps the most important and neglected aspect of human communication, the art of actually listening, the only form of communicating that helps solve problems and simultaneously enhance relationships; one of communicating’s most important purposes whether at home, school or in the workplace.</p>
    <p>- Learn About Active Listening<br>- Learn How to Communicate Authentically<br>- Learn the 10 keys to Sustaining Effective Communications</p>
    <h5>Session 2 - Goal Setting Workshop</h5>
    <p>Research studies show a direct link between goals and enhanced performance in life. Goals help us focus and allocate our time and resources efficiently, and they can keep us motivated when we feel like giving up. They help us stay aware of what is expected from us and leave little room for us to hide behind the curtain of unspecified expectations.</p>
    <p>In our Goal Setting Workshop we focus on the six reasons why goal setting is so important, using the <b>AIM SMART goal setting framework</b> we enable program participants to set effective goals - both large and small - and hold themselves accountable for attaining them.</p>
  </div>

  <div class="fold" style="left:246.67px"></div>
  <div class="fold" style="left:493.33px"></div>
  <div class="band band--inside"></div>
</section>

</body>
</html>
```